Mobile welding fabrication and repair, heavy equipment and semi repair

We need a business card design that will catch the eye but look prelesional at the same time. Were based out of Idaho and we do all welding fabrication jobs and repairs, we also build and install custom pipe fences for personal or larger scale fence jobs and can give free quotes. We can do semi truck and trailer repairs Mobily also.

Target Market(s)

Welding

Industry/Entity Type

welding and repair

Contact Information for Business Card

email (lanternforgeandfix@mailbay.net, phone number 208-471-3862, owner (Dalton Venkroff), Pipe Fence, Semi Repair, Mobile welding and fabrication

Font styles to use
Sans Serif

Requirements
Must have
• My logo in black background on one side , and other side my logo in white back round with all the information listed on card details
Nice to have
• make it stand out from other business cards

```html
<!DOCTYPE html>
<html lang="en">
<head>
<meta charset="utf-8">
<title>Lantern Forge and Fix — Business Card</title>
<link href="https://fonts.googleapis.com/css2?family=Lato:wght@400;700;900&display=swap" rel="stylesheet">
<style>
  :root {
    --bg: #2a2a2c;
    --paper: #f7f7f8;
    --ink: #2b2b2e;
    --ink-soft: #55565a;
    --brand-blue: #1473cf;
    --blue-light: #1aa0dc;
    --blue-deep: #0a4cae;
    --rule: #d3d4d8;
    --white: #ffffff;
  }
  * { box-sizing: border-box; margin: 0; padding: 0; }
  html, body { width: 1200px; height: 900px; overflow: hidden; }
  body {
    background: var(--bg);
    font-family: "Lato", sans-serif;
    display: flex;
    align-items: center;
    justify-content: center;
    gap: 40px;
  }
  .card {
    position: relative;
    width: 540px;
    height: 309px;
    border-radius: 4px;
    overflow: hidden;
    box-shadow: 0 14px 30px rgba(0,0,0,0.45);
  }

  /* Contact side */
  .card--front { background: var(--paper); color: var(--ink); }
  .front__brand {
    position: absolute;
    top: 58px;
    right: 58px;
    width: 290px;
    text-align: center;
  }
  .brand-name {
    font-weight: 900;
    text-transform: uppercase;
    letter-spacing: 0.04em;
    line-height: 1.05;
  }
  .front__brand .brand-name { color: var(--brand-blue); font-size: 34px; }
  .front__rule {
    position: absolute;
    left: 58px;
    right: 58px;
    top: 168px;
    height: 1px;
    background: var(--rule);
  }
  .front__person {
    position: absolute;
    left: 58px;
    top: 190px;
  }
  .person__name {
    color: var(--brand-blue);
    font-weight: 700;
    font-size: 22px;
    text-transform: uppercase;
    letter-spacing: 0.02em;
  }
  .person__role { color: var(--ink-soft); font-size: 14px; margin-top: 2px; }
  .contact-list { list-style: none; margin-top: 14px; }
  .contact-list li {
    display: flex;
    align-items: center;
    gap: 8px;
    font-size: 14px;
    color: var(--ink);
    line-height: 1.5;
  }
  .contact-list svg { width: 14px; height: 14px; flex: none; }

  /* Brand side */
  .card--back {
    background: linear-gradient(150deg, var(--blue-light) 0%, #137ed2 45%, var(--blue-deep) 100%);
    color: var(--white);
  }
  .back__brand {
    position: absolute;
    top: 92px;
    left: 0;
    right: 0;
    text-align: center;
  }
  .back__brand .brand-name { font-size: 38px; color: var(--white); }
  .back__services {
    position: absolute;
    left: 0;
    right: 0;
    bottom: 40px;
    text-align: center;
    font-size: 12.5px;
    letter-spacing: 0.03em;
    text-transform: uppercase;
  }
  .back__services .dot {
    display: inline-block;
    width: 7px; height: 7px;
    border-radius: 50%;
    background: var(--white);
    margin: 0 6px;
    vertical-align: middle;
  }
</style>
</head>
<body>
  <section class="card card--front" aria-label="Contact side">
    <div class="front__brand">
      <p class="brand-name">Lantern Forge<br>and Fix</p>
    </div>
    <div class="front__rule"></div>
    <div class="front__person">
      <p class="person__name">Dalton Venkroff</p>
      <p class="person__role">Owner</p>
      <ul class="contact-list">
        <li>
          <svg viewBox="0 0 24 24" aria-hidden="true"><path fill="#1473cf" d="M6.6 10.8a15.1 15.1 0 0 0 6.6 6.6l2.2-2.2a1 1 0 0 1 1-.25 11.4 11.4 0 0 0 3.6.57 1 1 0 0 1 1 1V20a1 1 0 0 1-1 1A17 17 0 0 1 3 4a1 1 0 0 1 1-1h3.5a1 1 0 0 1 1 1c0 1.25.2 2.45.57 3.6a1 1 0 0 1-.25 1z"/></svg>
          208-471-3862
        </li>
        <li>
          <svg viewBox="0 0 24 24" aria-hidden="true"><rect x="2" y="5" width="20" height="14" rx="1" fill="#1473cf"/><path d="M2 6l10 7 10-7" fill="none" stroke="#fff" stroke-width="1.6"/></svg>
          lanternforgeandfix@mailbay.net
        </li>
      </ul>
    </div>
  </section>

  <section class="card card--back" aria-label="Brand side">
    <div class="back__brand">
      <p class="brand-name">Lantern Forge<br>and Fix</p>
    </div>
    <p class="back__services">
      Pipe Fence<span class="dot"></span>Semi Repair<span class="dot"></span>Mobile Welding<span class="dot"></span>Fabrication
    </p>
  </section>
</body>
</html>
```